Billboard for a Contractor in Minnesota

Creating our first billboard that will be displayed on a freeway. Will be used on a digital Glint Signboard. Sign should be a 846 x 234 design. Our website is kestrel-paving.com Looking for something specific to "Look us up" or "Call" for your free concrete & asphalt estimate. Needs both web addresses (kestrel-paving.com and kestrel-masonry.com. Needs our phone number, logo. Our slogan is Serving All Your Asphalt & Concrete Needs. It's also our 25 Anniversary.

Target Market(s)

Residential Homeowners in the Twin Cities

Colors
abd036

Requirements
Must have
• Logo, Phone Number, Our Services, Web Addresses (both) Our services are all on our website. (Asphalt Driveway, Concrete Driveway, Concrete Apron, Concrete Sidewalk, Concrete Patio. Colors should be same as website. Black, White, Gray and the Neon Green color.

```html
<!DOCTYPE html>
<html lang="en">
<head>
<meta charset="utf-8">
<title>Kestrel Billboard</title>
<link rel="stylesheet" href="https://fonts.googleapis.com/css2?family=Montserrat:wght@400;500;700;800;900&family=Oswald:wght@600;700&family=Open+Sans:wght@400;600;700&display=swap">
<style>
  :root {
    --neon: #55cc46;
    --white: #ffffff;
    --paper: #f3f3f3;
    --ink: #111111;
    --bar: #333333;
    --silver-light: #f2f2f2;
    --silver-dark: #9a9a9a;
    --seal-ring: #a9a9a9;
    --seal-core: #2f8a5f;
    --stage: #e6e6e6;
  }
  * { margin: 0; padding: 0; box-sizing: border-box; }
  html, body { width: 1200px; height: 960px; overflow: hidden; }
  body { background: var(--stage); position: relative; font-family: "Montserrat", sans-serif; }

  .billboard {
    position: absolute; left: 40px; top: 316px;
    width: 1120px; height: 328px;
    background: var(--white);
    box-shadow: 0 14px 30px rgba(0,0,0,.25);
    overflow: hidden;
  }
  .billboard__art { position: absolute; left: 0; top: 0; width: 1120px; height: 266px; }

  .brand {
    position: absolute; left: 24px; top: 0; width: 300px; height: 266px;
    display: flex; align-items: center; justify-content: center; gap: 12px;
  }
  .brand__dot { width: 26px; height: 26px; border-radius: 50%; background: var(--ink); }
  .brand__name { font-family: "Montserrat", sans-serif; font-weight: 800; font-size: 52px; letter-spacing: 2px; color: var(--ink); }

  .headline { position: absolute; left: 422px; top: 32px; color: var(--white); }
  .headline__lead { font-family: "Montserrat", sans-serif; font-weight: 900; font-size: 29px; letter-spacing: 1.5px; line-height: 1; }
  .headline__main {
    display: inline-block; white-space: nowrap;
    font-family: "Oswald", sans-serif; font-weight: 700; font-size: 46px; line-height: 1.1;
    transform: scaleX(.92); transform-origin: left center;
  }

  .services { position: absolute; left: 430px; top: 143px; width: 660px; height: 60px; }
  .service {
    position: absolute; font-size: 18px; font-weight: 500; letter-spacing: -.3px; color: #222; white-space: nowrap;
    display: flex; align-items: center; gap: 3px;
  }
  .service svg { width: 15px; height: 15px; flex: none; }
  .service--c1 { left: 0; }
  .service--c2 { left: 231px; }
  .service--c3 { left: 465px; }
  .service--r1 { top: 0; }
  .service--r2 { top: 30px; }

  .offer {
    position: absolute; left: 431px; top: 222px; color: var(--white);
    font-size: 22px; font-weight: 500; white-space: nowrap; line-height: 34px;
  }
  .offer strong { font-size: 31px; font-weight: 800; }

  .contact-bar {
    position: absolute; left: 0; top: 266px; width: 1120px; height: 62px;
    background: var(--bar); color: var(--white);
    font-family: "Open Sans", sans-serif;
  }
  .contact-bar__web { position: absolute; top: 0; height: 62px; display: flex; align-items: center; gap: 10px; font-size: 26px; font-weight: 600; }
  .contact-bar__web svg { width: 24px; height: 24px; }
  .contact-bar__divider { position: absolute; left: 660px; top: 12px; width: 2px; height: 38px; background: #bdbdbd; }
  .contact-bar__call { position: absolute; left: 688px; top: 0; height: 62px; display: flex; align-items: center; font-size: 35px; font-weight: 700; white-space: nowrap; }
  .contact-bar__call span { color: var(--neon); margin-right: 10px; }
</style>
</head>
<body>
  <div class="billboard">
    <svg class="billboard__art" viewBox="0 0 1120 266" aria-hidden="true">
      <defs>
        <linearGradient id="silver" x1="0" x2="1" y1="0" y2="0">
          <stop offset="0" stop-color="#9a9a9a"/>
          <stop offset=".5" stop-color="#f2f2f2"/>
          <stop offset="1" stop-color="#b9b9b9"/>
        </linearGradient>
      </defs>
      <rect x="300" y="0" width="820" height="131" fill="#55cc46"/>
      <rect x="300" y="131" width="820" height="77" fill="#ffffff"/>
      <rect x="300" y="208" width="820" height="58" fill="#55cc46"/>
      <path d="M0 0 H398 Q478 133 412 266 H0 Z" fill="url(#silver)"/>
      <path d="M0 0 H352 Q432 133 370 266 H0 Z" fill="#55cc46"/>
      <path d="M0 0 H334 Q410 133 350 266 H0 Z" fill="#f3f3f3"/>
      <circle cx="1028" cy="63" r="78" fill="#ffffff"/>
      <circle cx="1028" cy="63" r="68" fill="#a9a9a9"/>
      <circle cx="1028" cy="63" r="55" fill="#2f8a5f"/>
    </svg>

    <div class="brand">
      <div class="brand__dot"></div>
      <div class="brand__name">KESTREL</div>
    </div>

    <div class="headline">
      <div class="headline__lead">SERVING ALL YOUR</div>
      <div class="headline__main">ASPHALT &amp; CONCRETE NEEDS</div>
    </div>

    <div class="services">
      <div class="service service--c1 service--r1"><svg viewBox="0 0 16 16"><path d="M2 9 L6 13 L14 3" fill="none" stroke="#55cc46" stroke-width="2"/></svg>ASPHALT DRIVEWAY</div>
      <div class="service service--c2 service--r1"><svg viewBox="0 0 16 16"><path d="M2 9 L6 13 L14 3" fill="none" stroke="#55cc46" stroke-width="2"/></svg>CONCRETE DRIVEWAY</div>
      <div class="service service--c3 service--r1"><svg viewBox="0 0 16 16"><path d="M2 9 L6 13 L14 3" fill="none" stroke="#55cc46" stroke-width="2"/></svg>CONCRETE APRON</div>
      <div class="service service--c1 service--r2"><svg viewBox="0 0 16 16"><path d="M2 9 L6 13 L14 3" fill="none" stroke="#55cc46" stroke-width="2"/></svg>CONCRETE SIDEWALK</div>
      <div class="service service--c2 service--r2"><svg viewBox="0 0 16 16"><path d="M2 9 L6 13 L14 3" fill="none" stroke="#55cc46" stroke-width="2"/></svg>CONCRETE PATIO</div>
    </div>

    <div class="offer">CALL FOR YOUR <strong>FREE</strong> CONCRETE &amp; ASPHALT ESTIMATE</div>

    <div class="contact-bar">
      <div class="contact-bar__web" style="left:36px">
        <svg viewBox="0 0 24 24"><g fill="none" stroke="#55cc46" stroke-width="2"><circle cx="12" cy="12" r="10"/><ellipse cx="12" cy="12" rx="4.5" ry="10"/><path d="M2 12 H22 M4 7 H20 M4 17 H20"/></g></svg>
        Kestrel-Paving.com
      </div>
      <div class="contact-bar__web" style="left:342px">
        <svg viewBox="0 0 24 24"><g fill="none" stroke="#55cc46" stroke-width="2"><circle cx="12" cy="12" r="10"/><ellipse cx="12" cy="12" rx="4.5" ry="10"/><path d="M2 12 H22 M4 7 H20 M4 17 H20"/></g></svg>
        Kestrel-Masonry.com
      </div>
      <div class="contact-bar__divider"></div>
      <div class="contact-bar__call"><span>CALL US:</span>555-014-2876</div>
    </div>
  </div>
</body>
</html>
```